The name of the company is Harbor Turns buying foreclosed homes and remodeling

A sleek classy card. It’s a home remodel and house flip company. Something mostly black with dark gray and red in color . Something with two f”s as a logo on front as shown in pictures. Kind of just let you guys run with it . I left a few pictures that should help
You guys get an idea of what I thought was good also left all the information for back of the card

Target Market(s)

Home remodel consumers

Industry/Entity Type

Construction Company

Contact Information for Business Card

All details are on photo

Font styles to use
Decorative

Colors

Designer to choose colors to be used in the design.

Requirements
Must have
• Name of company on front. Harbor Turns
Nice to have
• Up to you guys I trust you
Should not have
• Not sure

```html
<!DOCTYPE html>
<html lang="en">
<head>
<meta charset="utf-8">
<title>Harbor Turns – Business Card</title>
<link href="https://fonts.googleapis.com/css2?family=Michroma&family=Arimo:wght@400;700&family=Open+Sans:wght@400;600&display=swap" rel="stylesheet">
<style>
  :root {
    --backdrop: #1c1d20;
    --card: #222427;
    --card-edge: #2c2e32;
    --silver: #b9bcc1;
    --silver-dark: #6f7378;
    --white: #f1f1f1;
    --red: #d4202a;
  }
  * { margin: 0; padding: 0; box-sizing: border-box; }
  html, body { width: 1200px; height: 800px; overflow: hidden; }
  body {
    background: var(--backdrop);
    position: relative;
    font-family: "Arimo", Arial, sans-serif;
  }
  .card {
    position: absolute;
    width: 600px;
    height: 343px;
    background: var(--card);
    border: 1px solid var(--card-edge);
    box-shadow: 0 18px 40px rgba(0,0,0,.55);
  }
  .card--front { left: 90px; top: 60px; }
  .card--back  { left: 510px; top: 400px; }

  .brand {
    position: absolute;
    left: 0; right: 0; top: 50%;
    transform: translateY(-50%);
    display: flex;
    align-items: center;
    justify-content: center;
    gap: 18px;
  }
  .brand__mark {
    width: 22px; height: 22px;
    background: var(--silver);
  }
  .brand__name {
    font-family: "Michroma", sans-serif;
    font-size: 34px;
    color: var(--silver);
    letter-spacing: 1px;
  }

  .details {
    position: absolute;
    inset: 0;
    display: flex;
    flex-direction: column;
    align-items: center;
    justify-content: center;
    text-align: center;
    gap: 9px;
    color: var(--white);
  }
  .details__name {
    font-family: "Michroma", sans-serif;
    font-size: 23px;
    letter-spacing: .5px;
    margin-bottom: 4px;
  }
  .details__line { font-size: 14px; }
  .details__label { color: var(--red); font-weight: 700; }
  .details__web {
    font-family: "Open Sans", sans-serif;
    font-size: 15px;
    letter-spacing: 6px;
    margin-top: 6px;
  }
  .details__tagline {
    font-family: "Open Sans", sans-serif;
    font-size: 15px;
    letter-spacing: 3px;
    margin-top: 6px;
  }
  .details__dots { color: var(--red); }
</style>
</head>
<body>
  <section class="card card--front" aria-label="Card front">
    <div class="brand">
      <span class="brand__mark"></span>
      <span class="brand__name">Harbor Turns</span>
    </div>
  </section>

  <section class="card card--back" aria-label="Card back">
    <div class="details">
      <p class="details__name">Daniel Whitcombe JR</p>
      <p class="details__line"><span class="details__label">Phone:</span> 5550142876 | <span class="details__label">Email:</span> dwhitcombejr@mailbox.com</p>
      <p class="details__line"><span class="details__label">instagram:</span> Harbor_Turns_</p>
      <p class="details__web">www.harborturns.com</p>
      <p class="details__tagline">General contractor and Home Remodel<span class="details__dots">....</span></p>
    </div>
  </section>
</body>
</html>
```